Bref créative
Business Cards and Stationery Project
Verdant Pathways Health and Fitness Center
I need double sided standard sized Business Card [3.5" x 2"]
Use same fonts as used on my logo but also try different fonts
Professional
Marcus T. Delaney
Owner/Health Practitioner
4172 Larchmont Ave S
Minneapolis, MN 55405
marcus.delaney@vpwellbody.com
www.vpwellbody.com
Looking for a clean looking business card/stationery. It would be nice to have health center tagline w/ company name one one side. Tagline Where optimum health is your greatest wealth. If possible can there be date and time space for appointment.

```html
<!DOCTYPE html>
<html lang="en">
<head>
<meta charset="utf-8">
<title>Verdant Pathways Stationery</title>
<link href="https://fonts.googleapis.com/css2?family=Open+Sans:wght@400;600;700&display=swap" rel="stylesheet">
<style>
:root{
  --bg-center:#8d917a;
  --bg-edge:#4a4d3d;
  --paper:#ffffff;
  --green:#8cc63f;
  --green-dark:#5e9b22;
  --blue:#1f4fa0;
  --ink:#555a5e;
  --faint:#e6ecdf;
  --label:#e8ead8;
}
*{margin:0;padding:0;box-sizing:border-box}
html,body{width:1200px;height:439px;overflow:hidden}
body{font-family:"Open Sans",Arial,sans-serif;color:var(--ink)}
.board{position:relative;width:1200px;height:439px;
  background:radial-gradient(ellipse at 50% 45%,var(--bg-center) 0%,var(--bg-edge) 100%)}
.piece{position:absolute;background:var(--paper);box-shadow:2px 3px 6px rgba(0,0,0,.45);overflow:hidden}
.wave{position:absolute;left:0;bottom:0;width:100%}
.brand{display:flex;align-items:center;gap:4px;color:var(--green-dark);font-weight:700;white-space:nowrap}
.brand .dot{border-radius:50%;background:var(--green);flex:none}
.faint-mark{position:absolute;border-radius:50%;background:var(--faint)}
.label{position:absolute;font-size:7px;color:var(--label)}
/* business card */
.biz-card{left:29px;top:58px;width:182px;height:100px}
.biz-card .brand{position:absolute;left:12px;top:48px;font-size:10px}
.biz-card .brand .dot{width:12px;height:12px}
.biz-card .tagline{position:absolute;left:28px;top:63px;font-size:4.5px;color:var(--blue);white-space:nowrap}
.biz-card .contact{position:absolute;right:8px;top:6px;font-size:4px;line-height:1.4;text-align:right;white-space:nowrap}
/* appointment cards */
.appt-white{left:19px;top:180px;width:173px;height:108px}
.appt-green{left:19px;top:295px;width:173px;height:96px;background:linear-gradient(160deg,var(--green) 0%,var(--green-dark) 100%)}
.appt-title{position:absolute;top:8px;left:0;width:100%;text-align:center;font-size:7px;font-weight:700;color:var(--green-dark)}
.appt-green .appt-title{color:#fff}
.appt-lines{position:absolute;left:12px;right:12px;top:24px;font-size:5px}
.appt-lines .row{display:flex;gap:4px;margin-bottom:7px}
.appt-lines .row span{flex:1;border-bottom:.6px solid currentColor}
.appt-lines .row b{font-weight:600}
.appt-green .appt-lines{color:#fff}
.appt-note{position:absolute;left:0;width:100%;bottom:8px;text-align:center;font-size:4.5px}
/* letterheads */
.letterhead{top:34px;width:201px;height:357px}
.letterhead.a{left:298px}
.letterhead.b{left:533px;width:199px}
.letterhead .brand{position:absolute;left:12px;top:14px;font-size:8px}
.letterhead .brand .dot{width:10px;height:10px}
.letterhead .contact{position:absolute;right:10px;top:12px;font-size:4px;line-height:1.4;text-align:right}
.letterhead .faint-mark{left:28px;top:60px;width:110px;height:110px}
/* envelopes */
.env{left:864px;width:298px}
.env-1{top:34px;height:106px}
.env-2{top:139px;height:101px;background:linear-gradient(180deg,var(--green) 0%,var(--green-dark) 100%)}
.env-3{top:252px;height:91px}
.env-4{left:840px;top:336px;width:192px;height:91px}
.env .brand{font-size:7px}
.env .brand .dot{width:9px;height:9px}
.env-1 .brand{position:absolute;left:112px;top:24px}
.env-1 .url{position:absolute;left:112px;top:40px;font-size:4.5px}
.env-4 .brand{position:absolute;left:14px;top:10px}
.env-4 .faint-mark{left:132px;top:8px;width:50px;height:50px}
.env .flap{position:absolute;left:0;top:0;width:100%;height:100%}
</style>
</head>
<body>
<main class="board">

  <section class="piece biz-card">
    <div class="contact">Marcus T. Delaney<br>Owner/Health Practitioner<br>4172 Larchmont Ave S<br>Minneapolis, MN 55405<br>marcus.delaney@vpwellbody.com<br>www.vpwellbody.com</div>
    <div class="brand"><span class="dot"></span>Verdant Pathways</div>
    <div class="tagline">Where optimum health is your greatest wealth.</div>
    <svg class="wave" viewBox="0 0 182 30" height="30" preserveAspectRatio="none">
      <path d="M0 30 L0 22 C60 26 120 22 182 4 L182 30Z" fill="var(--green)"/>
      <path d="M0 22 C60 26 120 22 182 4 L182 8 C120 26 60 29 0 25Z" fill="var(--blue)"/>
    </svg>
  </section>

  <section class="piece appt-white">
    <div class="appt-title">Next Appointment</div>
    <div class="appt-lines">
      <div class="row"><b>Date</b><span></span></div>
      <div class="row"><b>Time</b><span></span></div>
      <div class="row"><b>Day</b><span></span></div>
    </div>
    <div class="appt-note">Please call 24 hours to reschedule</div>
  </section>

  <section class="piece appt-green">
    <div class="appt-title">Next Appointment</div>
    <div class="appt-lines">
      <div class="row"><b>Date</b><span></span></div>
      <div class="row"><b>Time</b><span></span></div>
      <div class="row"><b>Day</b><span></span></div>
    </div>
  </section>

  <span class="label" style="left:60px;top:410px">Business Cards A</span>

  <section class="piece letterhead a">
    <div class="faint-mark" role="img" aria-label="Faint brand emblem area"></div>
    <div class="brand"><span class="dot"></span>Verdant Pathways</div>
    <div class="contact">4172 Larchmont Ave S<br>Minneapolis, MN 55405<br>www.vpwellbody.com</div>
    <svg class="wave" viewBox="0 0 201 60" height="60" preserveAspectRatio="none">
      <path d="M0 60 L0 30 C70 10 140 14 201 34 L201 60Z" fill="var(--green)"/>
      <path d="M0 26 C70 6 140 10 201 30 L201 34 C140 14 70 10 0 30Z" fill="var(--blue)"/>
    </svg>
  </section>
  <span class="label" style="left:370px;top:396px">Letterhead A</span>

  <section class="piece letterhead b">
    <div class="faint-mark" role="img" aria-label="Faint brand emblem area"></div>
    <div class="brand"><span class="dot"></span>Verdant Pathways</div>
    <div class="contact">4172 Larchmont Ave S<br>Minneapolis, MN 55405<br>www.vpwellbody.com</div>
    <svg class="wave" viewBox="0 0 199 60" height="60" preserveAspectRatio="none">
      <path d="M0 60 L0 34 C60 14 140 10 199 28 L199 60Z" fill="var(--green)"/>
      <path d="M0 30 C60 10 140 6 199 24 L199 28 C140 10 60 14 0 34Z" fill="var(--blue)"/>
    </svg>
  </section>
  <span class="label" style="left:605px;top:396px">Letterhead B</span>

  <section class="piece env env-1">
    <div class="brand"><span class="dot"></span>Verdant Pathways</div>
    <div class="url">www.vpwellbody.com</div>
    <svg class="wave" viewBox="0 0 298 106" height="106" preserveAspectRatio="none">
      <path d="M0 0 L298 0 L298 8 C200 4 100 6 0 8Z" fill="var(--blue)"/>
      <path d="M0 106 L0 84 C100 100 200 100 298 86 L298 106Z" fill="var(--blue)"/>
    </svg>
  </section>

  <section class="piece env env-2">
    <svg class="flap" viewBox="0 0 298 101" preserveAspectRatio="none">
      <path d="M0 0 L149 62 L298 0" fill="none" stroke="#fff" stroke-width="1"/>
    </svg>
  </section>

  <section class="piece env env-3">
    <svg class="flap" viewBox="0 0 298 91" preserveAspectRatio="none">
      <path d="M0 0 L149 56 L298 0" fill="none" stroke="#cfd6c8" stroke-width="1"/>
      <path d="M0 91 L120 40 M298 91 L178 40" fill="none" stroke="#e2e6dc" stroke-width="1"/>
    </svg>
  </section>

  <section class="piece env env-4">
    <div class="faint-mark" role="img" aria-label="Faint brand emblem area"></div>
    <div class="brand"><span class="dot"></span>Verdant Pathways</div>
    <svg class="wave" viewBox="0 0 192 24" height="24" preserveAspectRatio="none">
      <path d="M0 24 L0 12 C60 2 130 2 192 14 L192 24Z" fill="var(--green)"/>
      <path d="M0 9 C60 -1 130 -1 192 11 L192 14 C130 2 60 2 0 12Z" fill="var(--blue)"/>
    </svg>
  </section>
  <span class="label" style="left:1110px;top:410px">Envelope Set</span>

</main>
</body>
</html>
```